Scrap Metal Recycling

We are looking for a simple yet bold business card. We already have the logo, please see attached. Color scheme of blue, black and white or just blue and white.

```html
<!DOCTYPE html>
<html lang="en">
<head>
<meta charset="utf-8">
<title>Ridgeway Metals Inc. – Business Card</title>
<link href="https://fonts.googleapis.com/css2?family=Arimo:wght@400;700&display=swap" rel="stylesheet">
<style>
  :root {
    --stage: #e9e9ea;
    --card: #39393a;
    --facet-1: #414142;
    --facet-2: #464647;
    --facet-3: #3e3e3f;
    --emboss: #2c2c2d;
    --white: #ffffff;
    --blue: #1b8fb8;
  }
  * { box-sizing: border-box; margin: 0; padding: 0; }
  html, body { width: 1200px; height: 912px; overflow: hidden; }
  body {
    background: var(--stage);
    font-family: "Arimo", Arial, sans-serif;
    display: flex;
    align-items: center;
    justify-content: center;
    gap: 40px;
  }
  .card {
    position: relative;
    width: 540px;
    height: 308px;
    border-radius: 16px;
    background: var(--card);
    overflow: hidden;
    box-shadow: 0 6px 18px rgba(0,0,0,.18);
  }
  /* Back side */
  .card--back .brand {
    position: absolute;
    left: 0; right: 0; top: 118px;
    text-align: center;
  }
  .card--back .brand-name {
    font-size: 32px;
    font-weight: 700;
    color: var(--emboss);
    letter-spacing: .5px;
  }
  .card--back .brand-tagline {
    margin-top: 6px;
    font-size: 14px;
    letter-spacing: 6px;
    color: var(--emboss);
  }
  /* Front side */
  .facets { position: absolute; inset: 0; }
  .card--front .brand {
    position: absolute;
    left: 36px;
    top: 112px;
  }
  .brand-row { display: flex; align-items: center; gap: 8px; }
  .brand-dot {
    width: 12px; height: 12px; border-radius: 50%;
    background: var(--blue);
  }
  .card--front .brand-name {
    font-size: 22px;
    font-weight: 700;
    color: var(--white);
    white-space: nowrap;
  }
  .card--front .brand-tagline {
    margin-top: 4px;
    font-size: 11px;
    letter-spacing: 4.5px;
    color: var(--blue);
    white-space: nowrap;
  }
  .holder {
    position: absolute;
    right: 44px;
    top: 54px;
    text-align: right;
  }
  .holder-name {
    font-size: 20px;
    font-weight: 700;
    color: var(--white);
    letter-spacing: .3px;
    white-space: nowrap;
  }
  .holder-title {
    margin-top: 3px;
    font-size: 13px;
    color: var(--blue);
    white-space: nowrap;
  }
  .accent-bar {
    position: absolute;
    right: 24px;
    top: 52px;
    width: 12px;
    height: 26px;
    background: var(--blue);
  }
  .contact {
    position: absolute;
    left: 36px;
    bottom: 22px;
    color: var(--white);
    font-size: 13px;
    line-height: 18px;
    list-style: none;
  }
  .contact-address { margin-bottom: 2px; }
  .contact-item { display: flex; align-items: center; gap: 8px; }
  .contact-icon { width: 11px; height: 11px; flex: none; }
</style>
</head>
<body>

  <section class="card card--back" aria-label="Card back">
    <div class="brand">
      <div class="brand-name">RIDGEWAY METALS INC.</div>
      <div class="brand-tagline">SCRAP METAL RECYCLING</div>
    </div>
  </section>

  <section class="card card--front" aria-label="Card front">
    <svg class="facets" viewBox="0 0 540 308" aria-hidden="true">
      <polygon points="320,0 540,0 540,308 300,308" fill="var(--facet-3)"/>
      <polygon points="320,0 430,0 470,55 430,160 540,240 540,308 410,308 310,240" fill="var(--facet-1)"/>
      <polygon points="430,0 540,0 540,180 500,205 430,160 470,55" fill="var(--facet-2)"/>
    </svg>

    <div class="brand">
      <div class="brand-row">
        <span class="brand-dot"></span>
        <span class="brand-name">RIDGEWAY METALS INC.</span>
      </div>
      <div class="brand-tagline">SCRAP METAL RECYCLING</div>
    </div>

    <span class="accent-bar"></span>
    <div class="holder">
      <div class="holder-name">MARCUS HALE</div>
      <div class="holder-title">Founder &amp; CEO</div>
    </div>

    <ul class="contact">
      <li class="contact-address">1480 Foundry Road<br>Harlan County 4417</li>
      <li class="contact-item">
        <svg class="contact-icon" viewBox="0 0 12 12"><path d="M2.5 1l2 2.2-1 1.3a7 7 0 0 0 4 4l1.3-1 2.2 2-1.3 1.5C5.5 11 1 6.5 1 2.3z" fill="var(--blue)"/></svg>
        123-555-01870
      </li>
      <li class="contact-item">
        <svg class="contact-icon" viewBox="0 0 12 12"><rect x="3" y="0.5" width="6" height="11" rx="1" fill="none" stroke="var(--blue)" stroke-width="1.2"/><circle cx="6" cy="9.5" r=".7" fill="var(--blue)"/></svg>
        123-555-01870
      </li>
      <li class="contact-item">
        <svg class="contact-icon" viewBox="0 0 12 12"><rect x="0.5" y="2" width="11" height="8" fill="var(--blue)"/><path d="M0.5 2l5.5 4.5L11.5 2" fill="none" stroke="var(--card)" stroke-width="1"/></svg>
        info@ridgewaymetals.com
      </li>
      <li class="contact-item">
        <svg class="contact-icon" viewBox="0 0 12 12"><circle cx="6" cy="6" r="5.5" fill="var(--blue)"/><path d="M0.5 6h11M6 0.5c-3 3-3 8 0 11M6 0.5c3 3 3 8 0 11" fill="none" stroke="var(--card)" stroke-width=".8"/></svg>
        www.ridgewaymetals.com
      </li>
    </ul>
  </section>

</body>
</html>
```